Painting Contractor Business Card Design

We are looking for a cool, bold, modern, polished, business card design. We are a high-end residential painting contractor. Please incorporate our logo and keep with our green/black color scheme. We are interested in seeing 2-sided and 1-sided options. Thank you very much!

Industry/Entity Type

Business

Contact Information for Business Card

Info for the card:
Owen Talsky
mobile 206-555-0193
email owen@kestrowfinish.net
web www.kestrowfinish.net

```html
<!DOCTYPE html>
<html lang="en">
<head>
<meta charset="utf-8">
<title>Kestrow Finish — Business Card</title>
<link href="https://fonts.googleapis.com/css2?family=Lato:wght@400;700;900&display=swap" rel="stylesheet">
<style>
  :root {
    --brand-green: #3dab4a;
    --brand-green-deep: #2f8f3b;
    --ink: #141414;
    --paper: #ffffff;
    --paper-shade: #e9e9e9;
    --backdrop: #eeeeea;
  }
  * { margin: 0; padding: 0; box-sizing: border-box; }
  html, body {
    width: 1200px; height: 900px; overflow: hidden;
    background: var(--backdrop);
    font-family: "Lato", sans-serif;
  }
  .sheet {
    width: 1200px; height: 900px;
    display: flex; flex-direction: column;
    align-items: center; justify-content: center; gap: 56px;
  }
  .card {
    width: 600px; height: 343px;
    border-radius: 4px; overflow: hidden; position: relative;
    box-shadow: 0 6px 18px rgba(0,0,0,0.14);
  }

  /* Back side */
  .card-back {
    background: radial-gradient(ellipse at 50% 45%, #45b553 0%, var(--brand-green) 45%, var(--brand-green-deep) 100%);
    display: flex; align-items: center; justify-content: center; gap: 16px;
  }
  .card-back .mark-square {
    width: 26px; height: 26px; background: var(--paper);
  }
  .card-back .brand-name {
    color: var(--paper); font-weight: 900; font-size: 40px;
    letter-spacing: 2px; text-transform: uppercase;
  }

  /* Front side */
  .card-front { background: var(--brand-green); }
  .front-top {
    height: 152px;
    background: radial-gradient(ellipse at 55% 40%, var(--paper) 0%, #f7f7f7 50%, var(--paper-shade) 100%);
    display: flex; align-items: center; justify-content: center; gap: 14px;
    padding-top: 14px;
  }
  .front-top .mark-square {
    width: 22px; height: 22px; background: var(--brand-green);
  }
  .front-top .brand-name {
    color: var(--ink); font-weight: 900; font-size: 34px;
    letter-spacing: 1px; text-transform: uppercase;
  }
  .front-bottom {
    display: flex; justify-content: center; gap: 34px;
    padding: 22px 30px 0; color: var(--paper);
  }
  .identity { text-align: right; }
  .identity .person-name { font-size: 25px; font-weight: 400; line-height: 1.1; }
  .identity .person-role { font-size: 16px; margin-bottom: 10px; }
  .identity .address { font-size: 18px; line-height: 1.3; }
  .contact-list { list-style: none; padding-top: 2px; }
  .contact-list li {
    display: flex; align-items: center; gap: 8px;
    font-size: 15px; line-height: 1; margin-bottom: 6px;
  }
  .contact-icon {
    width: 16px; height: 16px; background: var(--paper);
    border-radius: 2px; flex: none;
    display: flex; align-items: center; justify-content: center;
  }
  .contact-icon svg { width: 12px; height: 12px; }
</style>
</head>
<body>
<main class="sheet">

  <section class="card card-back" aria-label="Card back">
    <span class="mark-square"></span>
    <span class="brand-name">Kestrow Finish</span>
  </section>

  <section class="card card-front" aria-label="Card front">
    <header class="front-top">
      <span class="mark-square"></span>
      <span class="brand-name">Kestrow Finish</span>
    </header>
    <div class="front-bottom">
      <div class="identity">
        <p class="person-name">Owen Talsky</p>
        <p class="person-role">Managing Director</p>
        <p class="address">418 Alder Street<br>Seattle, 98101</p>
      </div>
      <ul class="contact-list">
        <li>
          <span class="contact-icon">
            <svg viewBox="0 0 12 12"><path d="M3 1.5 L4.6 3.6 L3.8 4.6 Q5 7 7.4 8.2 L8.4 7.4 L10.5 9 L9.6 10.5 Q4.5 10 1.5 2.4 Z" fill="#3dab4a"/></svg>
          </span>206-555-0193
        </li>
        <li>
          <span class="contact-icon">
            <svg viewBox="0 0 12 12"><rect x="3" y="1" width="6" height="3" fill="#3dab4a"/><rect x="1" y="4.5" width="10" height="4" rx="1" fill="#3dab4a"/><rect x="3" y="7.5" width="6" height="3.5" fill="#3dab4a"/></svg>
          </span>206-555-0194
        </li>
        <li>
          <span class="contact-icon">
            <svg viewBox="0 0 12 12"><rect x="1" y="2.5" width="10" height="7" fill="#3dab4a"/><path d="M1 2.5 L6 6.5 L11 2.5" fill="none" stroke="#fff" stroke-width="1"/></svg>
          </span>owen@kestrowfinish.net
        </li>
        <li>
          <span class="contact-icon">
            <svg viewBox="0 0 12 12"><path d="M5 7 L7 5 M4.2 5.6 L2.6 7.2 a1.6 1.6 0 0 0 2.2 2.2 L6.4 7.8 M5.6 4.2 L7.2 2.6 a1.6 1.6 0 0 1 2.2 2.2 L7.8 6.4" fill="none" stroke="#3dab4a" stroke-width="1.3" stroke-linecap="round"/></svg>
          </span>www.kestrowfinish.net
        </li>
      </ul>
    </div>
  </section>

</main>
</body>
</html>
```